ZEPRILO.COM is a premium domain sales company. Our competitors are companies like vastplots.example, getparcels.example, peerwords.example. Our current site is at www.zeprilos.example.

We want to have the ability to search for domains, to highlight special offers and have some testimonials on the index page.

The logo for the site is attached.

Please be sure that the order form fits on the screen without scrolling the page. I want the entire form, including the submit button to fit without any page scrolling.

Delivered product - INDEX PAGE, ORDER FORM AND CONTENT PAGE PSDs.

Target Market(s)

Small to Medium business professionals

Industry/Entity Type

It Company

Requirements
Must have
• 1. List of domains for sale
2. Simple search box with button to run the search
3. link for advanced search
4. testimonial area. Note - this can be a small box where a different testimonial is displayed on each page load.
Nice to have
• Would like the site to have some white space. Don't want a heavily packed website. Give it an "airy" feel.

```html
<!DOCTYPE html>
<html lang="en">
<head>
<meta charset="utf-8">
<title>ZEPRILO.COM – Premium Domains</title>
<link href="https://fonts.googleapis.com/css2?family=Open+Sans:ital,wght@0,400;0,600;0,700;1,400;1,700&display=swap" rel="stylesheet">
<style>
:root{
  --topbar:#2e2e2e;
  --ink:#333;
  --green:#1c7a3a;
  --brand-green:#238a3e;
  --blue:#1766b0;
  --navy:#0b2e5c;
  --hero-a:#0a2c57;
  --hero-b:#0f4d8c;
  --panel:#0c2d55;
  --panel-head:#0e4a90;
  --band:#151515;
  --row-alt:#f3f3f3;
  --line:#e3e3e3;
  --footer:#3a3a3a;
  --footer-dark:#2c2c2c;
  --white:#fff;
}
*{box-sizing:border-box;margin:0;padding:0}
html,body{width:754px;height:1200px;overflow:hidden}
body{font-family:"Open Sans",Arial,sans-serif;color:var(--ink);background:var(--white);position:relative}
.topbar{position:absolute;top:0;left:0;width:754px;height:38px;background:var(--topbar);border-bottom:3px solid #ddd}
.social-mini{position:absolute;left:62px;top:15px;display:flex;gap:10px}
.social-mini span{width:7px;height:7px;background:#777;border-radius:1px}
.top-phone{position:absolute;left:536px;top:11px;color:#fff;font-weight:600;font-size:12px;display:flex;align-items:center;gap:5px}
.top-cart{position:absolute;left:644px;top:11px;color:#fff;font-weight:600;font-size:12px;display:flex;align-items:center;gap:5px}
.header{position:absolute;top:38px;left:0;width:754px;height:60px;background:#fff}
.logo{position:absolute;left:62px;top:18px;font-size:23px;font-weight:700;color:var(--navy);letter-spacing:-.5px}
.nav{position:absolute;right:62px;top:25px;display:flex;gap:23px;font-size:9px;color:#555}
.nav .active{color:#222;position:relative}
.nav .active::before{content:"";position:absolute;left:-4px;right:-4px;top:-27px;height:3px;background:var(--brand-green)}
.hero{position:absolute;top:98px;left:0;width:754px;height:378px;background:radial-gradient(ellipse at 35% 45%,#2c79c2 0%,var(--hero-b) 35%,var(--hero-a) 80%)}
.hero h1{position:absolute;left:62px;top:20px;color:#fff;font-style:italic;font-weight:700;font-size:19.5px;letter-spacing:-.3px}
.hero-art{position:absolute;left:92px;top:62px;width:300px;height:292px;background:linear-gradient(160deg,#8ea4bd 0%,#6f86a3 50%,#3d5d86 100%);opacity:.85}
.order{position:absolute;left:440px;top:18px;width:251px;height:343px;background:var(--panel)}
.order h2{background:var(--panel-head);color:#fff;font-size:9.5px;font-weight:700;line-height:12.5px;padding:6px 30px 5px 12px;height:34px}
.fields{position:relative;padding:12px 13px 0}
.f{display:block;height:14px;background:#fff;border:1px solid #9bb;font-size:6.5px;font-style:italic;color:#333;padding:0 6px;line-height:12px;margin-bottom:8.8px}
.row{display:flex;gap:9px;align-items:center}
.cards{display:flex;gap:3px}
.cards span{width:19px;height:11px;border-radius:1px}
.exp{font-size:6.5px;font-style:italic;color:#fff;margin-bottom:8.8px}
.sel{height:13px;background:#fff;font-size:6.5px;font-style:italic;padding:0 5px;line-height:12px;display:flex;justify-content:space-between}
.help{color:#6fd08a;font-size:5.5px;text-decoration:underline;font-style:italic}
.place{display:flex;align-items:center;gap:10px;margin-top:2px}
.btn-order{background:var(--brand-green);color:#fff;font-size:10px;padding:1px 7px;border-radius:2px;border:1px solid #55b06c}
.place p{font-size:6px;font-style:italic;color:#fff;line-height:7px;width:125px}
.search{position:absolute;top:476px;left:0;width:754px;height:60px;background:var(--band)}
.s-input{position:absolute;left:62px;top:13px;width:470px;height:29px;background:#fff;font-style:italic;font-size:12px;color:#333;padding:6px 6px;border:1px solid #999}
.s-tld{position:absolute;left:543px;top:13px;width:60px;height:29px;background:#fff;font-size:12px;padding:5px 7px;display:flex;justify-content:space-between}
.s-btn{position:absolute;left:614px;top:13px;width:77px;height:29px;background:var(--panel-head);border:1px solid #2b6fbd;color:#fff;font-weight:600;font-size:12px;text-align:center;line-height:27px}
.adv{position:absolute;left:467px;top:44px;color:#fff;font-size:8px;font-style:italic;text-decoration:underline}
.listing{position:absolute;left:62px;top:560px;width:629px;border-collapse:collapse;font-size:8.4px;border:1px solid #f0f0f0}
.listing th{font-weight:400;text-align:left;height:46px;padding-left:6px;color:#444;border-right:1px solid var(--line)}
.listing td{height:31px;padding-left:6px;color:#555;border-right:1px solid var(--line)}
.listing th:first-child,.listing td:first-child{padding-left:13px}
.listing tr:nth-child(even) td{background:var(--row-alt)}
.listing th:last-child,.listing td:last-child{border-right:0}
.listing td.dom{color:var(--green)}
.listing td.dom::before{content:"";display:inline-block;width:3px;height:3px;background:#111;border-radius:50%;margin-right:7px;vertical-align:middle}
.listing td.price{color:var(--blue)}
.info{display:block;width:8px;height:8px;border-radius:50%;background:#5e8fce;border:1px solid #2e5f9e;margin-left:24px}
.about{position:absolute;left:62px;top:903px;width:430px}
.about h3,.testi h3{font-weight:400;color:var(--blue);font-size:19px}
.about h3 small{font-size:13px}
.about p{font-size:8.6px;line-height:13px;color:#444;margin-top:10px}
.about h3+p{margin-top:12px}
.testi{position:absolute;left:513px;top:900px;width:178px}
.testi blockquote{font-style:italic;font-size:7.6px;line-height:16.3px;color:#444;margin-top:9px;padding-left:17px;position:relative}
.testi blockquote::before{content:"\201C";position:absolute;left:2px;top:-3px;font-size:17px;font-weight:700}
.testi blockquote::after{content:"\201D";position:absolute;right:-6px;bottom:-10px;font-size:17px;font-weight:700}
.footer{position:absolute;top:1052px;left:0;width:754px;height:148px;background:var(--footer)}
.fcol{position:absolute;top:16px;height:85px;border-right:1px solid #4a4a4a}
.fcol h4{font-weight:400;color:#fff;font-size:12.5px;margin-bottom:7px}
.fcol li{list-style:none;color:#ccc;font-size:7.8px;line-height:11.2px}
.fcall{position:absolute;right:63px;top:38px;text-align:right;color:#ddd;font-size:11px;line-height:16px}
.fsoc{position:absolute;right:63px;top:75px;display:flex;gap:5px}
.fsoc span{width:16px;height:16px;border-radius:2px}
.copy{position:absolute;left:0;bottom:0;width:754px;height:33px;background:var(--footer-dark);color:#ccc;font-size:7.8px;text-align:center;line-height:27px}
</style>
</head>
<body>
<div class="topbar">
  <div class="social-mini"><span></span><span></span><span></span><span></span></div>
  <div class="top-phone">
    <svg width="11" height="12" viewBox="0 0 12 12"><path d="M3 1l2 2.5-1.2 1.3c.7 1.5 1.8 2.6 3.3 3.3L8.4 6.9 11 9l-1.3 2C5 11 1 7 1 2.3z" fill="#fff"/></svg>1400.555.019</div>
  <div class="top-cart">
    <svg width="13" height="11" viewBox="0 0 13 11"><path d="M0 1h2l2 6h7l1.5-4.5H3" fill="none" stroke="#fff" stroke-width="1.2"/><circle cx="5" cy="9.5" r="1" fill="#fff"/><circle cx="10" cy="9.5" r="1" fill="#fff"/></svg>CART</div>
</div>

<header class="header">
  <div class="logo">ZEPRILO.COM</div>
  <nav class="nav">
    <span class="active">HOME</span><span>DELETING DOMAINS</span><span>DOMAINS FOR SALE</span><span>TESTIMONIALS</span><span>SUPPORT</span>
  </nav>
</header>

<section class="hero">
  <h1>Find the best name for your business...</h1>
  <div class="hero-art" role="img" aria-label="Illustration: a silver globe built from jigsaw puzzle pieces, some missing"></div>
  <form class="order">
    <h2>PLEASE SUBMIT ALL FIELDS TO COMPLETE YOUR ORDER</h2>
    <div class="fields">
      <div class="row"><span class="f" style="width:108px">Enter your first name</span><span class="f" style="width:108px">Enter your last name</span></div>
      <span class="f">Enter your email address</span>
      <span class="f">Enter your phone number</span>
      <div class="row" style="gap:5px"><span class="f" style="width:138px">Enter your card number</span>
        <div class="cards" style="margin-bottom:8.8px"><span style="background:#3a78c4"></span><span style="background:#e6e6e6"></span><span style="background:#2a3c8c"></span><span style="background:#f4f4f4"></span></div></div>
      <span class="f">Enter your card name</span>
      <div class="row exp" style="gap:8px">Expiration Date:
        <span class="sel" style="width:38px;color:#333">Month <b>▾</b></span>
        <span class="sel" style="width:38px;color:#333">Year <b>▾</b></span>
        <span class="sel" style="width:38px;color:#333">CVV</span>
        <span class="help">What's This?</span></div>
      <span class="f">Enter your address</span>
      <span class="f">Address line 2</span>
      <span class="f">Enter your city/town</span>
      <span class="f">Enter your state/province</span>
      <span class="f">Enter your zip/postal code</span>
      <span class="f" style="display:flex;justify-content:space-between">Select your country <b>▾</b></span>
      <div class="place"><span class="btn-order">Place Order</span><p>Secure your domains when you click the button above.</p></div>
    </div>
  </form>
</section>

<section class="search">
  <div class="s-input">Enter Domain Name...</div>
  <div class="s-tld">.com <span>▾</span></div>
  <div class="s-btn">SEARCH</div>
  <span class="adv">Advanced Search</span>
</section>

<table class="listing">
  <colgroup><col style="width:275px"><col style="width:111px"><col style="width:107px"><col style="width:76px"><col style="width:60px"></colgroup>
  <tr><th>Domain name</th><th>Creat date</th><th>Expire date</th><th>Price</th><th>More Info</th></tr>
  <tr><td class="dom">GlowPanels.example</td><td>22 - 5 - 2013</td><td>22 - 5 - 2014</td><td class="price">$85.00</td><td><i class="info"></i></td></tr>
  <tr><td class="dom">JobHorizon.example</td><td>22 - 5 - 2013</td><td>22 - 5 - 2014</td><td class="price">$85.00</td><td><i class="info"></i></td></tr>
  <tr><td class="dom">NoteMarker.example</td><td>22 - 5 - 2013</td><td>22 - 5 - 2014</td><td class="price">$85.00</td><td><i class="info"></i></td></tr>
  <tr><td class="dom">HeartBeacon.example</td><td>22 - 5 - 2013</td><td>22 - 5 - 2014</td><td class="price">$85.00</td><td><i class="info"></i></td></tr>
  <tr><td class="dom">KeenFolio.example</td><td>22 - 5 - 2013</td><td>22 - 5 - 2014</td><td class="price">$85.00</td><td><i class="info"></i></td></tr>
  <tr><td class="dom">LayerHost.example</td><td>22 - 5 - 2013</td><td>22 - 5 - 2014</td><td class="price">$85.00</td><td><i class="info"></i></td></tr>
  <tr><td class="dom">PairSeek.example</td><td>22 - 5 - 2013</td><td>22 - 5 - 2014</td><td class="price">$85.00</td><td><i class="info"></i></td></tr>
  <tr><td class="dom">GlowPanels.example</td><td>22 - 5 - 2013</td><td>22 - 5 - 2014</td><td class="price">$85.00</td><td><i class="info"></i></td></tr>
  <tr><td class="dom">JobHorizon.example</td><td>22 - 5 - 2013</td><td>22 - 5 - 2014</td><td class="price">$85.00</td><td><i class="info"></i></td></tr>
</table>

<section class="about">
  <h3>About ZEPRILO<small>.com</small></h3>
  <p>Le Lorem Ipsum est simplement du faux texte employé dans la composition et la mise en page avant impression. Le Lorem Ipsum est le faux texte standard de l'imprimerie depuis les années 1500, quand un peintre anonyme assembla ensemble des morceaux de texte pour réaliser un livre spécimen de polices de texte.</p>
  <p>Il n'a pas fait que survivre cinq siècles, mais s'est aussi adapté à la bureautique informatique, sans que son contenu n'en soit modifié. Il a été popularisé dans les années 1960.</p>
</section>

<aside class="testi">
  <h3>Testimonials</h3>
  <blockquote>Le Lorem Ipsum est simplement du faux texte employé dans la composition et la mise en page avant impressione Lorem Ipsum est le faux texte standard de l'imprimerie depuis les années 1500.</blockquote>
</aside>

<footer class="footer">
  <div class="fcol" style="left:62px;width:96px"><h4>DOMAINS</h4><ul><li>Categories</li><li>Sell Your Domains</li></ul></div>
  <div class="fcol" style="left:198px;width:89px"><h4>DOMAINS</h4><ul><li>Plusieurs</li><li>structures</li><li>phrases</li><li>touches</li><li>aléatoires</li></ul></div>
  <div class="fcol" style="left:321px;width:84px"><h4>COMPANY</h4><ul><li>About</li><li>Contact</li><li>Policies</li></ul></div>
  <div class="fcol" style="left:429px;width:75px"><h4>SUITES</h4><ul><li>Contrairement</li><li>répandue</li><li>intéressé</li><li>étudiant</li><li>incontestable</li></ul></div>
  <div class="fcall">Call our domain Expert today<br>5400.555.118 Or +1 2400 555 207</div>
  <div class="fsoc"><span style="background:#2c5aa8"></span><span style="background:#1d74b5"></span><span style="background:#3aa5e0"></span></div>
  <div class="copy">© Copyrights 2013 All rights Reserved</div>
</footer>
</body>
</html>
```